Business card design Needed for new logo / Construction business, home extensions and new builds

We need a business card design using our new logo files which i will attach to this project :)

We are a small construction business specialising in home extensions, new builds and property development. We are very ambitious and would appreciate professional and elegant designs for our new business card.

Very serious about using the services on BriefNest and recently acquired our new logo from here :)

Please get involved, i will feedback when i can as i am very busy but can respond daily, thanks

Target Market(s)

People that want to build onto their houses, new building developments or adding too their existing property

Industry/Entity Type

Construction

Contact Information for Business Card

Hollin Marsh Construction, Tobias Renwick (Managing Director), Tel 07822200444, email - info@hollin-marsh, www.hollin-marsh.co.uk

Colors

Designer to choose colors to be used in the design.

Requirements
Must have
• I like a deep grey on the back please. A lot of you have provided black from and back, try mixing things up a little. The black looks cool 😎 Thanks

```html
<!DOCTYPE html>
<html lang="en">
<head>
<meta charset="utf-8">
<title>Hollin Marsh Construction – Business Card</title>
<link rel="stylesheet" href="https://fonts.googleapis.com/css2?family=Open+Sans:wght@400;600&display=swap">
<style>
  :root {
    --page: #e6e3de;
    --card-front: #0a0a0a;
    --card-back: #2a2a2a;
    --card-back-light: #363636;
    --pattern: #17130c;
    --pattern-on-grey: #332b1d;
    --gold: #d39b2b;
    --silver: #cfcfcf;
    --grey-text: #c4c4c4;
    --bronze: #5a4522;
  }
  * { box-sizing: border-box; margin: 0; padding: 0; }
  html, body { width: 1200px; height: 1113px; overflow: hidden; }
  body {
    background: var(--page);
    font-family: "Open Sans", Arial, sans-serif;
    display: flex;
    flex-direction: column;
    align-items: center;
    justify-content: center;
    gap: 33px;
  }
  .card {
    position: relative;
    width: 880px;
    height: 500px;
    overflow: hidden;
    box-shadow: 0 10px 24px rgba(0,0,0,0.25);
  }
  .front { background: var(--card-front); }
  .back { background: var(--card-back); }
  .pattern-band {
    position: absolute;
    background: linear-gradient(135deg, var(--pattern), #0e0c08);
  }
  /* front */
  .front .pattern-left { left: 0; top: 0; width: 110px; height: 250px; }
  .front .pattern-right { right: 0; bottom: 0; width: 150px; height: 280px; }
  .brand {
    position: absolute;
    left: 0; right: 0; top: 150px;
    display: flex;
    align-items: center;
    justify-content: center;
    gap: 16px;
  }
  .brand-square { width: 22px; height: 22px; background: var(--gold); flex: none; }
  .brand-name {
    font-weight: 600;
    font-size: 40px;
    letter-spacing: 2px;
    color: var(--gold);
    text-transform: uppercase;
    white-space: nowrap;
  }
  .services {
    position: absolute;
    left: 20px; right: 20px; top: 300px;
    display: flex;
    justify-content: center;
    align-items: stretch;
  }
  .service {
    font-size: 12px;
    letter-spacing: 0.5px;
    color: var(--silver);
    text-transform: uppercase;
    white-space: nowrap;
    padding: 5px 12px;
  }
  .service-divider { width: 4px; background: var(--bronze); flex: none; }
  /* back */
  .back .halftone {
    position: absolute; left: 0; top: 0; width: 520px; height: 360px;
    background: radial-gradient(ellipse at 20% 20%, var(--card-back-light), var(--card-back) 70%);
  }
  .back .pattern-right {
    right: 0; top: 160px; width: 140px; height: 340px;
    background: linear-gradient(135deg, var(--pattern-on-grey), var(--card-back));
  }
  .back .brand { left: 60px; right: auto; top: 120px; justify-content: flex-start; }
  .back .brand-name { font-size: 34px; }
  .person {
    position: absolute; right: 170px; top: 205px; text-align: right;
  }
  .person-name { font-weight: 600; font-size: 30px; color: var(--gold); }
  .person-role { font-size: 18px; color: var(--grey-text); margin-top: 2px; }
  .contacts {
    position: absolute; right: 170px; top: 315px;
    list-style: none;
    display: flex; flex-direction: column; gap: 9px;
  }
  .contact {
    display: flex; align-items: center; justify-content: flex-end; gap: 12px;
    font-size: 15px; color: var(--silver); white-space: nowrap;
  }
  .contact svg { width: 16px; height: 16px; fill: var(--gold); flex: none; }
</style>
</head>
<body>

<section class="card front">
  <div class="pattern-band pattern-left" role="img" aria-label="Fine gold diagonal line pattern"></div>
  <div class="pattern-band pattern-right" role="img" aria-label="Fine gold diagonal line pattern"></div>
  <div class="brand">
    <span class="brand-square"></span>
    <span class="brand-name">Hollin Marsh Construction</span>
  </div>
  <div class="services">
    <span class="service">Construction Consultant</span>
    <span class="service-divider"></span>
    <span class="service">House Renovation</span>
    <span class="service-divider"></span>
    <span class="service">Architecture &amp; Building</span>
    <span class="service-divider"></span>
    <span class="service">Pre Construction Planning</span>
  </div>
</section>

<section class="card back">
  <div class="halftone" role="img" aria-label="Subtle halftone dot texture"></div>
  <div class="pattern-band pattern-right" role="img" aria-label="Fine gold diagonal line pattern"></div>
  <div class="brand">
    <span class="brand-square"></span>
    <span class="brand-name">Hollin Marsh</span>
  </div>
  <div class="person">
    <p class="person-name">Tobias Renwick</p>
    <p class="person-role">Managing Director</p>
  </div>
  <ul class="contacts">
    <li class="contact">+44 7822 200 444
      <svg viewBox="0 0 24 24"><path d="M6.6 10.8a15 15 0 0 0 6.6 6.6l2.2-2.2a1 1 0 0 1 1-.25 11.4 11.4 0 0 0 3.6.57 1 1 0 0 1 1 1V20a1 1 0 0 1-1 1A17 17 0 0 1 3 4a1 1 0 0 1 1-1h3.5a1 1 0 0 1 1 1c0 1.25.2 2.45.57 3.57a1 1 0 0 1-.25 1z"/></svg>
    </li>
    <li class="contact">info@hollin-marsh.co.uk
      <svg viewBox="0 0 24 24"><path d="M2 5h20v14H2zm2 2v.5l8 5 8-5V7zm0 2.8V17h16V9.8l-8 5z"/></svg>
    </li>
    <li class="contact">www.hollin-marsh.co.uk
      <svg viewBox="0 0 24 24"><path d="M12 2a10 10 0 1 0 0 20 10 10 0 0 0 0-20zm6.9 9h-3a15 15 0 0 0-1.3-5.6A8 8 0 0 1 18.9 11zM12 4.1c.9 1.3 1.7 3.8 1.9 6.9h-3.8c.2-3.1 1-5.6 1.9-6.9zM9.4 5.4A15 15 0 0 0 8.1 11h-3a8 8 0 0 1 4.3-5.6zM5.1 13h3a15 15 0 0 0 1.3 5.6A8 8 0 0 1 5.1 13zm6.9 6.9c-.9-1.3-1.7-3.8-1.9-6.9h3.8c-.2 3.1-1 5.6-1.9 6.9zm2.6-1.3a15 15 0 0 0 1.3-5.6h3a8 8 0 0 1-4.3 5.6z"/></svg>
    </li>
    <li class="contact">Ferndale Road, Elmhurst, Wareham, BH7 4QL
      <svg viewBox="0 0 24 24"><path d="M12 2a7 7 0 0 0-7 7c0 5 7 13 7 13s7-8 7-13a7 7 0 0 0-7-7zm0 9.5A2.5 2.5 0 1 1 12 6.5a2.5 2.5 0 0 1 0 5z"/></svg>
    </li>
  </ul>
</section>

</body>
</html>
```